Verpackungen für doppelwandiges Glas im 2er Set
Zielgruppe
Wir produzieren Küchenartikel jeglicher Art.
Im konkreten Beispiel geht es um ein doppelwandiges Glas für Tee, Kaffee etc
Hochauflösende Bilder, Stanzkonturen, Logos, Barcodes und Texte stellen wir Ihnen natürlich bereit.
Aufgabenstellung
Die Verpackung soll sehr edel wirken.

```html
<!DOCTYPE html>
<html lang="de">
<head>
<meta charset="utf-8">
<title>Vitrella – Verpackung Doppelwandige Gläser 2er Set</title>
<link rel="stylesheet" href="https://fonts.googleapis.com/css2?family=Cinzel:wght@400&family=Lora:wght@400;600&display=swap">
<style>
  :root {
    --stage: #ececec;
    --panel-light: #f4f4f4;
    --panel-mid: #dcdcdc;
    --band: #1f1f1f;
    --ink: #2a2a2a;
    --ink-soft: #555555;
    --on-band: #f2f2f2;
    --edge: #cfcfcf;
  }
  * { margin: 0; padding: 0; box-sizing: border-box; }
  html, body {
    width: 1200px;
    height: 638px;
    overflow: hidden;
    background: var(--stage);
  }
  .canvas {
    position: relative;
    width: 1200px;
    height: 638px;
  }
  .packaging-net {
    position: absolute;
    left: 140px;
    top: 139px;
    display: flex;
    height: 360px;
    box-shadow: 0 18px 40px rgba(0,0,0,0.12);
  }
  .front-panel {
    position: relative;
    width: 620px;
    height: 360px;
    background: var(--panel-light);
    border-right: 1px solid var(--edge);
  }
  .product-photo {
    position: absolute;
    left: 0;
    top: 0;
    width: 620px;
    height: 218px;
    background: linear-gradient(180deg, #f5f5f5 0%, #e4e4e4 100%);
  }
  .brand-band {
    position: absolute;
    left: 0;
    bottom: 0;
    width: 620px;
    height: 142px;
    background: var(--band);
    display: flex;
    flex-direction: column;
    align-items: center;
    justify-content: center;
    gap: 10px;
  }
  .brand-name {
    display: flex;
    align-items: center;
    gap: 10px;
    font-family: "Cinzel", serif;
    font-size: 24px;
    letter-spacing: 0.14em;
    color: var(--on-band);
  }
  .brand-mark {
    width: 10px;
    height: 10px;
    background: var(--on-band);
  }
  .brand-rule {
    width: 150px;
    height: 1px;
    background: rgba(242,242,242,0.55);
  }
  .side-panel {
    position: relative;
    width: 300px;
    height: 360px;
    background: linear-gradient(135deg, #ffffff 0%, #f1f1f1 60%, #e6e6e6 100%);
    padding: 34px 28px;
    color: var(--ink);
    font-family: "Lora", serif;
  }
  .side-brand {
    font-family: "Cinzel", serif;
    font-size: 20px;
    letter-spacing: 0.1em;
    margin-bottom: 18px;
  }
  .side-title {
    font-size: 13px;
    font-weight: 600;
    margin-bottom: 16px;
  }
  .side-intro {
    font-size: 11px;
    color: var(--ink-soft);
    line-height: 1.5;
    margin-bottom: 14px;
  }
  .feature-list {
    list-style: none;
    font-size: 11px;
    line-height: 1.5;
    color: var(--ink-soft);
  }
  .feature-list li {
    position: relative;
    padding-left: 14px;
    margin-bottom: 6px;
  }
  .feature-list li::before {
    content: "";
    position: absolute;
    left: 0;
    top: 7px;
    width: 5px;
    height: 5px;
    border-radius: 50%;
    background: var(--ink);
  }
</style>
</head>
<body>
<main class="canvas">
  <section class="packaging-net">
    <div class="front-panel">
      <div class="product-photo" role="img" aria-label="Produktfoto: zwei doppelwandige Gläser nebeneinander auf hellgrauem Grund"></div>
      <div class="brand-band">
        <div class="brand-name"><span class="brand-mark"></span>VITRELLA</div>
        <div class="brand-rule"></div>
      </div>
    </div>
    <div class="side-panel">
      <div class="side-brand">VITRELLA</div>
      <h2 class="side-title">Doppelwandige Gläser – 2er Set 350 ml</h2>
      <p class="side-intro">Stilvolle Gläser für Tee, Kaffee und Cocktails</p>
      <ul class="feature-list">
        <li>mit Thermo-Effekt</li>
        <li>kondensfrei und angenehm griffig</li>
        <li>für kalte und heiße Getränke geeignet</li>
        <li>mundgeblasenes Borosilikatglas</li>
        <li>spülmaschinen- und mikrowellengeeignet</li>
      </ul>
    </div>
  </section>
</main>
</body>
</html>
```